Logo & Web Design for Technical Research Products

Logo and Web Design for a little business selling some niche research, technical products. Current site is at: http://mavrite-lab.com/mavrite-lab-ionic-bench-unit. The audience are university researchers, technical labs and similar.

We would like a more professional looking logo and design than what is currently there.

This new design should include/consider:
- A front page with the ability to show-case 2-3 select products
- An About Us page
- A Contact Us page
- An FAQ page
- A hierarchical menu structure (preferably to the left) allowing for at least two levels. (We plan to add more products and categories in the future)
- Include both a Desktop and Phone version (responsive design)
- We plan to have all products follow a similar template so please have that in mind when desiging (Some part of the product template may be omitted for some products if not applicable)
- Multiple images per product should be supported(carousel perhaps?)

When creating the CSS and HTML please use Bootstap 4.
(https://framelyt.dev/docs/4.0/getting-started/introduction/)

```html
<!DOCTYPE html>
<html lang="en">
<head>
<meta charset="utf-8">
<title>Mavrite Lab – Technical Research Products</title>
<link rel="stylesheet" href="https://fonts.googleapis.com/css2?family=Jost:wght@300;400;500;700&display=swap">
<style>
:root{
  --accent:#3ec1df;
  --ink:#111111;
  --body:#444444;
  --muted:#7a7a7a;
  --soft:#f4f8fb;
  --card:#f3f3f3;
  --line:#dedede;
  --star:#f0742d;
  --white:#ffffff;
}
*{box-sizing:border-box;margin:0;padding:0}
html,body{width:1200px;height:2955px;overflow:hidden}
body{font-family:"Jost",sans-serif;color:var(--body);background:var(--white);position:relative}
.abs{position:absolute}
.btn{position:absolute;background:var(--accent);color:var(--white);border-radius:20px;font-size:14px;font-weight:500;display:flex;align-items:center;justify-content:center;height:36px}
.accent{color:var(--accent)}
.wave{position:absolute;width:62px;height:12px}

/* header */
.site-header{position:absolute;top:0;left:0;width:1200px;height:71px;background:var(--white);box-shadow:0 2px 8px rgba(0,0,0,.06);z-index:2}
.brand{position:absolute;left:139px;top:16px;font-size:33px;font-weight:400;color:var(--accent)}
.main-nav{position:absolute;top:27px;font-size:13px;color:var(--ink)}
.main-nav.active{color:var(--accent)}

/* hero */
.hero{position:absolute;top:71px;left:0;width:1200px;height:529px;background:linear-gradient(90deg,#f1f3f6 0%,#eceff3 38%,#c9d0d8 60%,#9aa4ae 80%,#7d8690 100%)}
.hero h1{position:absolute;left:142px;top:138px;font-size:42px;line-height:55px;font-weight:700;color:var(--ink)}
.hero h1 span{font-weight:300;color:var(--accent)}
.hero p{position:absolute;left:142px;top:250px;width:380px;font-size:15px;line-height:26px;color:#333}

/* about */
.about-accent{position:absolute;left:134px;top:669px;width:366px;height:252px;background:var(--accent);clip-path:polygon(0 0,100% 0,0 100%)}
.about-photo{position:absolute;left:141px;top:676px;width:437px;height:323px;background:linear-gradient(135deg,#9fb5c9,#5d7d9d 55%,#3c5670)}
.sec-title{position:absolute;font-size:36px;font-weight:500;color:var(--ink)}
.about-text{position:absolute;left:623px;top:760px;width:434px;font-size:13px;line-height:23px;text-align:justify;color:#555}

/* products */
.products{position:absolute;top:1073px;left:0;width:1200px;height:645px;background:var(--soft)}
.card{position:absolute;top:1239px;width:211px;height:332px;background:var(--card);border:1px solid var(--line);box-shadow:0 10px 10px -8px rgba(0,0,0,.35);text-align:center}
.card .thumb{height:161px;background:var(--white);border-bottom:1px solid var(--line);display:flex;align-items:center;justify-content:center}
.card .thumb div{width:110px;height:110px;border-radius:4px}
.card .price{font-size:22px;color:#333;margin-top:12px}
.card .stars{color:var(--star);font-size:12px;letter-spacing:2px;margin-top:2px}
.card .name{font-size:17px;line-height:22px;color:#222;margin-top:6px;height:44px}
.card .buy{position:static;display:inline-flex;width:56px;height:28px;font-size:13px;margin-top:8px}
.arrow{position:absolute;top:1387px;width:28px;height:28px;border-radius:50%}

/* faq */
.faq-item{position:absolute;width:444px;height:42px;border:1px solid var(--line);background:var(--white);font-size:14.5px;color:#333;display:flex;align-items:center;padding-left:12px}
.faq-item .q{color:var(--accent);margin-right:6px}
.faq-item .plus{position:absolute;right:10px;top:8px;color:var(--accent);font-size:20px}
.faq-open{position:absolute;left:614px;top:1888px;width:444px;height:154px;background:var(--accent);color:var(--white);padding:10px 15px}
.faq-open .head{font-size:14.5px}
.faq-open p{font-size:13px;line-height:23px;margin-top:16px;text-align:justify}

/* contact */
.contact{position:absolute;top:2296px;left:0;width:1200px;height:468px;background:var(--soft)}
.field{position:absolute;font-size:13px;color:#555;border-bottom:1px solid #999;height:36px}
.info{position:absolute;left:808px;display:flex;align-items:center}
.info .ic{width:42px;height:42px;border:2px solid var(--accent);border-radius:50%;display:flex;align-items:center;justify-content:center;margin-right:13px}
.info .t{font-size:15px;color:#222;line-height:21px}
.info .t b{font-weight:500;font-size:14px}

/* footer */
.site-footer{position:absolute;top:2764px;left:0;width:1200px;height:191px;background:var(--accent);color:var(--white)}
.foot-nav{position:absolute;top:46px;font-size:13px}
.foot-rule{position:absolute;left:141px;top:96px;width:918px;height:1px;background:rgba(255,255,255,.8)}
.copy{position:absolute;left:141px;top:138px;font-size:13px}
.social{position:absolute;top:122px;width:40px;height:40px;border-radius:50%;background:var(--white)}
</style>
</head>
<body>

<header class="site-header">
  <div class="brand">Mavrite Lab</div>
  <nav>
    <span class="main-nav active" style="left:669px">Home</span>
    <span class="main-nav" style="left:748px">About Us</span>
    <span class="main-nav" style="left:842px">Products</span>
    <span class="main-nav" style="left:932px">Faq</span>
    <span class="main-nav" style="left:997px">Contact Us</span>
  </nav>
</header>

<section class="hero" role="img" aria-label="Photo of a young technician soldering a circuit board under a magnifier in a lab">
  <h1>Welcome To Technical<br>Research <span>Products</span></h1>
  <p>Lorem ipsum dolor sit amet, consectetuer adipiscing elit, sed diam nonummy nibh euismod tincidunt ut laoreet dolore magna aliquam erat volutpat.</p>
  <div class="btn" style="left:141px;top:347px;width:113px">Contact Us</div>
</section>

<section class="about">
  <div class="about-accent"></div>
  <div class="about-photo" role="img" aria-label="Photo of an engineer with glasses working on electronics with a screwdriver"></div>
  <h2 class="sec-title" style="left:623px;top:665px">About <span class="accent">Us</span></h2>
  <svg class="wave" style="left:622px;top:722px" viewBox="0 0 62 12"><path d="M2 6 C14 -1 24 13 38 6 S56 3 60 4" fill="none" stroke="#3ec1df" stroke-width="3" stroke-linecap="round"/></svg>
  <p class="about-text">Lorem ipsum dolor sit amet, consectetuer adipiscing elit, sed diam nonummy nibh euismod tincidunt ut laoreet dolore magna aliquam erat volutpat. Ut wisi enim ad minim veniam, quis nostrud exerci tation ullamcorper suscipit lobortis nisl ut aliquip ex ea commodo consequat. Duis autem vel eum iriure dolor in hendrerit in vulputate velit esse molestie consequat, vel illum dolore eu feugiat nulla facilisis at vero eros et accumsan et iusto odio dignissim qui blandit praesent luptatum zzril delenit augue duis dolore te feugait nulla facilisi.</p>
  <div class="btn" style="left:623px;top:963px;width:113px">Read More</div>
</section>

<section class="products">
  <h2 class="sec-title" style="left:0;width:1200px;text-align:center;top:69px">Our <span class="accent">Products</span></h2>
</section>
<svg class="wave" style="left:569px;top:1197px" viewBox="0 0 62 12"><path d="M2 6 C14 -1 24 13 38 6 S56 3 60 4" fill="none" stroke="#3ec1df" stroke-width="3" stroke-linecap="round"/></svg>

<svg class="arrow" style="left:84px;background:#b8b8b8" viewBox="0 0 28 28"><path d="M16 8 L10 14 L16 20" fill="none" stroke="#fff" stroke-width="2"/></svg>
<svg class="arrow" style="left:1088px;background:var(--accent)" viewBox="0 0 28 28"><path d="M12 8 L18 14 L12 20" fill="none" stroke="#fff" stroke-width="2"/></svg>

<article class="card" style="left:141px">
  <div class="thumb"><div role="img" aria-label="Photo of an eight channel battery tester rack" style="background:linear-gradient(#d9dcdc,#6f8a72)"></div></div>
  <div class="price">€ 2,700</div><div class="stars">★★★★☆</div>
  <div class="name">8 Channel Battery<br>Tester</div><div class="btn buy">Buy</div>
</article>
<article class="card" style="left:376px">
  <div class="thumb"><div role="img" aria-label="Photo of a flow battery test cell" style="background:linear-gradient(#7f9fd8,#3c63b8)"></div></div>
  <div class="price">€ 1,900</div><div class="stars">★★★★☆</div>
  <div class="name">Ionic Bench Unit<br>Test Cell</div><div class="btn buy">Buy</div>
</article>
<article class="card" style="left:611px">
  <div class="thumb"><div role="img" aria-label="Photo of a photoelectrochemical test cell" style="background:linear-gradient(#8a8a8a,#2a2a2a)"></div></div>
  <div class="price">€ 2,900</div><div class="stars">★★★★☆</div>
  <div class="name">Photoelectrochemical<br>laboratory test cell</div><div class="btn buy">Buy</div>
</article>
<article class="card" style="left:846px">
  <div class="thumb"><div role="img" aria-label="Photo of a two channel peristaltic pump" style="background:linear-gradient(#c8ccd0,#303a48)"></div></div>
  <div class="price">€ 2,700</div><div class="stars">★★★★☆</div>
  <div class="name">2 channel<br>peristaltic pump</div><div class="btn buy">Buy</div>
</article>

<div class="btn" style="left:551px;top:1613px;width:98px">View All</div>

<section class="faq">
  <h2 class="sec-title" style="left:0;width:1200px;text-align:center;top:1782px">Frequently Asked <span class="accent">Questions</span></h2>
  <svg class="wave" style="left:569px;top:1838px" viewBox="0 0 62 12"><path d="M2 6 C14 -1 24 13 38 6 S56 3 60 4" fill="none" stroke="#3ec1df" stroke-width="3" stroke-linecap="round"/></svg>

  <div class="faq-item" style="left:141px;top:1888px"><span class="q">Q :</span>1&nbsp; Lorem Ipsum Is Simply Dummy Text?<span class="plus">+</span></div>
  <div class="faq-item" style="left:141px;top:1943px"><span class="q">Q :</span>2&nbsp; Lorem Ipsum Is Simply Dummy Text?<span class="plus">+</span></div>
  <div class="faq-item" style="left:141px;top:1999px"><span class="q">Q :</span>3&nbsp; Lorem Ipsum Is Simply Dummy Text?<span class="plus">+</span></div>
  <div class="faq-item" style="left:141px;top:2055px"><span class="q">Q :</span>4&nbsp; Lorem Ipsum Is Simply Dummy Text?<span class="plus">+</span></div>
  <div class="faq-item" style="left:141px;top:2110px"><span class="q">Q :</span>5&nbsp; Lorem Ipsum Is Simply Dummy Text?<span class="plus">+</span></div>

  <div class="faq-open">
    <div class="head">Q : 6&nbsp; Lorem Ipsum Is Simply Dummy Text?<span style="position:absolute;right:10px;top:6px;font-size:20px">–</span></div>
    <p>Lorem Ipsum is simply dummy text of the printing and typesettink industry. Lorem Ipsum has been theml industry's standard dummy text ever since the 1500s, when ank unknown printer took a galley. Lorem Ipsum is simply dummy.</p>
  </div>
  <div class="faq-item" style="left:614px;top:2055px"><span class="q">Q :</span>7&nbsp; Lorem Ipsum Is Simply Dummy Text?<span class="plus">+</span></div>
  <div class="faq-item" style="left:614px;top:2110px"><span class="q">Q :</span>8&nbsp; Lorem Ipsum Is Simply Dummy Text?<span class="plus">+</span></div>

  <div class="btn" style="left:544px;top:2188px;width:112px">Read More</div>
</section>

<section class="contact">
  <h2 class="sec-title" style="left:142px;top:72px">Contact <span class="accent">Us</span></h2>
  <svg class="wave" style="left:141px;top:130px" viewBox="0 0 62 12"><path d="M2 6 C14 -1 24 13 38 6 S56 3 60 4" fill="none" stroke="#3ec1df" stroke-width="3" stroke-linecap="round"/></svg>

  <div class="field" style="left:143px;top:176px;width:249px">Name*</div>
  <div class="field" style="left:406px;top:176px;width:249px">Phone*</div>
  <div class="field" style="left:143px;top:232px;width:249px">Email*</div>
  <div class="field" style="left:406px;top:232px;width:249px">Company Name</div>
  <div class="field" style="left:143px;top:287px;width:514px;height:58px">Message*</div>
  <div class="btn" style="left:141px;top:378px;width:121px">Submit Now</div>

  <svg class="abs" style="left:726px;top:96px" width="12" height="312" viewBox="0 0 12 312">
    <circle cx="6" cy="5" r="4" fill="#3ec1df"/>
    <line x1="6" y1="10" x2="6" y2="302" stroke="#3ec1df" stroke-width="1.5" stroke-dasharray="5 4"/>
    <circle cx="6" cy="307" r="4" fill="#3ec1df"/>
  </svg>

  <div class="info" style="top:167px">
    <div class="ic"><svg width="18" height="20" viewBox="0 0 18 20"><path d="M9 19 C3 12 2 9 2 7 a7 7 0 0 1 14 0 c0 2 -1 5 -7 12z" fill="none" stroke="#3ec1df" stroke-width="2"/><circle cx="9" cy="7" r="2.4" fill="#3ec1df"/></svg></div>
    <div class="t">Mavrite Lab<br><b>123, lorem</b></div>
  </div>
  <div class="info" style="top:243px">
    <div class="ic"><svg width="20" height="20" viewBox="0 0 20 20"><path d="M4 2 l4 1 1 4 -2 2 c1 2 3 4 5 5 l2 -2 4 1 1 4 -2 2 C9 18 2 11 2 4z" fill="#3ec1df"/></svg></div>
    <div class="t">Call Us:<br><b>(123) 456 789</b></div>
  </div>
  <div class="info" style="top:315px">
    <div class="ic"><svg width="20" height="14" viewBox="0 0 20 14"><rect x="1" y="1" width="18" height="12" rx="1.5" fill="#3ec1df"/><path d="M1 2 L10 8 L19 2" fill="none" stroke="#fff" stroke-width="1.5"/></svg></div>
    <div class="t">Email Us:<br><b>info@mavritelab.com</b></div>
  </div>
</section>

<footer class="site-footer">
  <span class="foot-nav" style="left:405px;font-weight:500">Home</span>
  <span class="foot-nav" style="left:484px">About Us</span>
  <span class="foot-nav" style="left:577px">Products</span>
  <span class="foot-nav" style="left:668px">Faq</span>
  <span class="foot-nav" style="left:732px">Contact Us</span>
  <div class="foot-rule"></div>
  <div class="copy">© 2019 Mavrite Lab. All Rights Reserved.</div>
  <div class="social" style="left:879px" aria-label="Social link"></div>
  <div class="social" style="left:925px" aria-label="Social link"></div>
  <div class="social" style="left:972px" aria-label="Social link"></div>
  <div class="social" style="left:1018px" aria-label="Social link"></div>
</footer>

</body>
</html>
```